Flyer for a conference next week

We need a flyer to promote our stand at a conference next week - involving a Pebble Jar Contest.

The following files are attached:

- Existing Company Logos
- The logo of the product we are promoting (oVerla)
- A previous flyer - may be useful
- a Jellybean image (we want this to be the major part of the design

The flyer will be size : DL - 109mm x 220mm (5mm bleed) and 300 DPI

The flyer should include the following text :

"Take the Pebble Jar Contest at the Tallow Reef table in the exhibit space and win a Drone!"

"Find out more about our oVerla Web Services platform for Financial Models"

Colors
ed2e35

Requirements
Must have
• The flyer will be size : DL - 109mm x 220mm (5mm bleed) and 300 DPI
• The flyer should include the following text :
• "Take the Pebble Jar Contest at the Tallow Reef table in the exhibit space and win a Drone!"
• "Find out more about our oVerla Web Services platform for Financial Models"

```html
<!DOCTYPE html>
<html lang="en">
<head>
<meta charset="utf-8">
<title>Pebble Jar Contest Flyer</title>
<link href="https://fonts.googleapis.com/css2?family=Anton&family=Oswald:wght@500&family=Roboto:wght@400&display=swap" rel="stylesheet">
<style>
  :root {
    --brand-red: #ed2e35;
    --deep-red: #7a0f14;
    --ink: #141414;
    --white: #ffffff;
    --backdrop: #e6e6e6;
    --candy-red: #e8323a;
    --candy-yellow: #f5d52a;
    --candy-blue: #2aa6d9;
    --candy-green: #3fb54a;
    --candy-pink: #ef6fa0;
    --candy-orange: #f28a24;
  }
  * { margin: 0; padding: 0; box-sizing: border-box; }
  html, body { width: 1200px; height: 1200px; overflow: hidden; background: var(--backdrop); }
  .flyer {
    position: absolute; left: 320px; top: 35px;
    width: 560px; height: 1130px; overflow: hidden;
    background: var(--ink);
  }
  .candy-photo {
    position: absolute; inset: 0 0 220px 0;
    background:
      radial-gradient(circle at 20% 15%, var(--candy-red) 0, transparent 28%),
      radial-gradient(circle at 80% 25%, var(--candy-blue) 0, transparent 30%),
      radial-gradient(circle at 30% 55%, var(--candy-green) 0, transparent 28%),
      radial-gradient(circle at 75% 65%, var(--candy-pink) 0, transparent 30%),
      radial-gradient(circle at 50% 85%, var(--candy-yellow) 0, transparent 30%),
      linear-gradient(160deg, var(--candy-orange), var(--candy-red) 40%, var(--candy-blue) 70%, var(--candy-yellow));
  }
  .footer-band { position: absolute; left: 0; top: 0; width: 560px; height: 1130px; }
  .headline {
    position: absolute; left: 0; right: 0; top: 0;
    font-family: 'Anton', sans-serif; font-weight: 400;
    color: var(--white); letter-spacing: -2px; line-height: 1;
    -webkit-text-stroke: 2px var(--deep-red);
    text-shadow: 3px 4px 6px rgba(0,0,0,.55);
  }
  .headline .line {
    position: absolute; left: 0; right: 0;
    text-align: center; white-space: nowrap;
    font-size: 64px; transform: translateY(-50%);
  }
  .headline .line-1 { top: 203px; }
  .headline .line-2 { top: 326px; font-size: 112px; -webkit-text-stroke: 3px var(--deep-red); }
  .headline .line-3 { top: 428px; }
  .headline .line-4 { top: 516px; }
  .headline .line-5 { top: 599px; }
  .headline .line-6 { top: 683px; }
  .sponsor {
    position: absolute; top: 905px; left: 0; right: 0;
    display: flex; justify-content: center;
  }
  .sponsor-text { display: flex; flex-direction: column; }
  .sponsor-kicker { font-family: 'Oswald', sans-serif; font-weight: 500; font-size: 15px; color: var(--brand-red); line-height: 1.1; }
  .sponsor-name { font-family: 'Oswald', sans-serif; font-weight: 500; font-size: 30px; color: var(--white); line-height: 1.05; letter-spacing: 1px; }
  .tagline {
    position: absolute; top: 978px; left: 0; right: 0;
    text-align: center; font-family: 'Roboto', sans-serif;
    color: var(--white); font-size: 23px; line-height: 33px;
  }
  .web-address {
    position: absolute; top: 1052px; left: 0; right: 0;
    text-align: center; font-family: 'Roboto', sans-serif;
    color: var(--white); font-size: 24px; letter-spacing: .5px;
  }
</style>
</head>
<body>
  <div class="flyer">
    <div class="candy-photo" role="img" aria-label="Close-up photo of a heap of colourful jelly beans"></div>
    <svg class="footer-band" viewBox="0 0 560 1130" aria-hidden="true">
      <polygon points="0,815 560,890 560,1130 0,1130" fill="var(--ink)"/>
    </svg>
    <h1 class="headline">
      <span class="line line-1">Take the Pebble Jar</span>
      <span class="line line-2">Contest</span>
      <span class="line line-3">at the Tallow Reef</span>
      <span class="line line-4">table in the exhibit</span>
      <span class="line line-5">space and</span>
      <span class="line line-6">win a Drone!</span>
    </h1>
    <div class="sponsor">
      <div class="sponsor-text">
        <span class="sponsor-kicker">A PROGRAM FROM</span>
        <span class="sponsor-name">TALLOW REEF</span>
      </div>
    </div>
    <p class="tagline">Find out more about our oVerla<br>Web Services platform for Financial Models</p>
    <p class="web-address">www.tallowreef.com.au</p>
  </div>
</body>
</html>
```